Citrus grower needs label for rare fruit package

We are going to sell our rare fruit in a reusable lunch bag and need an informative, eye-catching imprint for the bag.

Target Market(s)

restaurant chefs, foodies
Our customers are adventurous and search out new and unusual things. A fresh, fun and original look will appeal to then.

Requirements
Must have
• One color only printed on a dark green background. See uploaded file for details.

There is no designated font! Use what you think will be bold, fun, fresh and easy to read.
Nice to have
• It would be nice if you could incorporate a tree design based on the attached photo of a giant tree on the ranch which is a local landmark.

```html
<!DOCTYPE html>
<html lang="en">
<head>
<meta charset="utf-8">
<title>Oak Hill Groves – California Finger Limes</title>
<link rel="stylesheet" href="https://fonts.googleapis.com/css2?family=Comic+Neue:wght@700&display=swap">
<style>
  :root {
    --bag-green: #175039;
    --ink-yellow: #f5f200;
  }
  html, body {
    margin: 0;
    padding: 0;
    width: 1200px;
    height: 1200px;
    overflow: hidden;
    background: var(--bag-green);
  }
  .label {
    display: block;
    width: 1200px;
    height: 1200px;
  }
  .label-text {
    font-family: "Comic Neue", "Comic Sans MS", cursive;
    font-weight: 700;
    fill: var(--ink-yellow);
    stroke: var(--ink-yellow);
    stroke-linejoin: round;
    paint-order: stroke fill;
    text-anchor: middle;
  }
  .label-text.contact { stroke-width: 3; }
  .label-text.phone { stroke-width: 4; }
  .label-text.small { stroke-width: 1.2; }
  .frame-outer { fill: none; stroke: var(--ink-yellow); stroke-width: 3; }
  .frame-inner { fill: none; stroke: var(--ink-yellow); stroke-width: 5; }
  .tree-area { fill: var(--ink-yellow); }
</style>
</head>
<body>
<svg class="label" viewBox="0 0 1200 1200" xmlns="http://www.w3.org/2000/svg">
  <rect class="frame-outer" x="66.5" y="59.5" width="1067" height="957"/>
  <rect class="frame-inner" x="82.5" y="74.5" width="1035" height="924" rx="36" ry="36"/>

  <g class="landmark-tree" role="img" aria-label="Silhouette of the ranch's giant landmark tree in yellow">
    <ellipse class="tree-area" cx="607" cy="375" rx="352" ry="275"/>
  </g>

  <text class="label-text contact site" x="613" y="737" font-size="62" textLength="582" lengthAdjust="spacingAndGlyphs">oak-hill-groves.com</text>
  <text class="label-text contact email" x="613" y="804" font-size="62" textLength="708" lengthAdjust="spacingAndGlyphs">oakhillgroves@mail.com</text>
  <text class="label-text phone" x="613" y="888" font-size="86" textLength="584" lengthAdjust="spacingAndGlyphs">555-014-2276</text>
  <text class="label-text contact product" x="613" y="957" font-size="58" textLength="694" lengthAdjust="spacingAndGlyphs">California&#160;&#160;Finger Limes</text>

  <text class="label-text small origin" x="599" y="1058" font-size="27" textLength="357" lengthAdjust="spacingAndGlyphs">Produce of California, USA</text>
  <text class="label-text small address" x="600" y="1091" font-size="27" textLength="543" lengthAdjust="spacingAndGlyphs">Oak Hill Groves,&#160;&#160;Ridgeview, CA 90000</text>
</svg>
</body>
</html>
```